Front & Back Book Cover Design

Title:
THE QUIET LANDLORD: How to Grow Comfort and Plenty Through Property Held by Others
Author:
Mel T. Varnak
Design Philosophy:
A modern, minimalist-luxury aesthetic that feels visionary and intelligent — positioned between business innovation (The Brisk Venture), modern finance (The Anatomy of Thrift), and timeless real estate insight (Bold Aunt Meek Aunt).
Think: clean, bold, and idea-driven — a visual reflection of the book’s central concept: wealth through clarity, not clutter.
Back Cover:
To include book description along with author photo and bio
Files:
PNG, PDF, EPUB

```html
<!DOCTYPE html>
<html lang="en">
<head>
<meta charset="utf-8">
<title>The Quiet Landlord — Mel T. Varnak</title>
<link rel="stylesheet" href="https://fonts.googleapis.com/css2?family=Noto+Serif:ital,wght@0,400;0,700;1,400&display=swap">
<style>
  :root {
    --page: #ffffff;
    --cover-black: #0d0e10;
    --cover-mid: #1b1c1f;
    --cover-grey: #3a3a3c;
    --gold-light: #f3d98a;
    --gold: #d6a935;
    --gold-deep: #b8861f;
    --white: #ffffff;
    --subtitle: #f1f1f1;
  }
  * { margin: 0; padding: 0; box-sizing: border-box; }
  html, body {
    width: 1200px; height: 1200px; overflow: hidden;
    background: var(--page);
  }
  .canvas { position: relative; width: 1200px; height: 1200px; }
  .cover {
    position: absolute; left: 246px; top: 66px;
    width: 716px; height: 1075px;
    overflow: hidden;
    font-family: "Noto Serif", Georgia, serif;
  }
  .cover-art {
    position: absolute; inset: 0;
    background:
      radial-gradient(ellipse at 92% 8%, rgba(80,80,82,0.55), transparent 45%),
      linear-gradient(100deg, var(--cover-black) 0%, var(--cover-mid) 58%, var(--cover-grey) 100%);
  }
  .gold-text {
    background: linear-gradient(180deg, var(--gold-light) 0%, var(--gold) 55%, var(--gold-deep) 100%);
    -webkit-background-clip: text; background-clip: text;
    color: transparent;
  }
  .title {
    position: absolute; left: 45px; top: 86px;
    font-weight: 700; line-height: 1;
    letter-spacing: 0.01em;
  }
  .title-line { display: block; }
  .title-the { font-size: 68px; }
  .title-quiet { font-size: 90px; color: var(--white); margin-top: 16px; }
  .title-landlord { font-size: 90px; margin-top: 0px; }
  .subtitle {
    position: absolute; left: 45px; top: 500px; width: 330px;
    text-align: center;
    font-style: italic; font-weight: 400;
    font-size: 23px; line-height: 35px;
    color: var(--subtitle);
    letter-spacing: 0.02em;
  }
  .author {
    position: absolute; left: 45px; top: 994px;
    font-size: 56px; font-weight: 400; line-height: 1;
    letter-spacing: 0.04em;
  }
</style>
</head>
<body>
<main class="canvas">
  <section class="cover" aria-label="Front cover of The Quiet Landlord">
    <div class="cover-art" role="img" aria-label="Black textured silhouette of a head in profile, edged with a thin gold line, set against a dark charcoal background"></div>
    <h1 class="title">
      <span class="title-line title-the gold-text">THE</span>
      <span class="title-line title-quiet">QUIET</span>
      <span class="title-line title-landlord gold-text">LANDLORD</span>
    </h1>
    <p class="subtitle">How to Grow Comfort and Plenty Through Property Held by Others</p>
    <p class="author gold-text">Mel T. Varnak</p>
  </section>
</main>
</body>
</html>
```